We need a fresh, new church business card!!

We need a church business card with basic info to hand out as invites. We are looking for something clean that communicates our basic information clearly.

We are open to square or rectangle card sizes.

General Public

Religious

The attached logo is the only one that I have available. We'd like to see options with with text of the logo lighter and on a dark background as well as options with white/light backgrounds.

Also, we'd like to see option with rounded corners.

• Address - 2718 Maple Row, Rockford, IL 61142
• Website - brookvane.example
• Phone - 815-555-0163
• Service times -
• Sunday - 10am Sunday School
• - 11am Family Worship
• - 6pm Night of Prayer
• Wednesday - 7:30pm Adult Bible Study
• Classes for all ages

```html
<!DOCTYPE html>
<html lang="en">
<head>
<meta charset="utf-8">
<title>Brookvane Pentecostal Church — Business Cards</title>
<link rel="stylesheet" href="https://fonts.googleapis.com/css2?family=Open+Sans:wght@400;600;700&display=swap">
<style>
  :root {
    --teal: #4b8b99;
    --teal-deep: #3d7684;
    --teal-light: #5f9dab;
    --white: #ffffff;
    --paper: #f4f5f5;
    --ink: #4a4f53;
    --stage: #e6e8e9;
  }
  * { box-sizing: border-box; margin: 0; padding: 0; }
  html, body {
    width: 1200px; height: 950px; overflow: hidden;
    background: var(--stage);
    font-family: "Open Sans", Arial, sans-serif;
  }
  .sheet { position: relative; width: 1200px; height: 950px; }
  .card {
    position: absolute; left: 250px; width: 700px; height: 400px;
    overflow: hidden; box-shadow: 0 6px 18px rgba(0,0,0,.18);
  }

  /* Back side */
  .card--back {
    top: 50px;
    background: linear-gradient(135deg, var(--teal-light), var(--teal) 55%, var(--teal-deep));
    color: var(--white); text-align: center;
  }
  .brand { display: flex; align-items: center; gap: 14px; }
  .brand__dot { width: 56px; height: 56px; border-radius: 50%; flex: none; }
  .brand__name { font-weight: 600; line-height: 1; text-transform: uppercase; }
  .brand__name span { display: block; }
  .brand__name .brand__main { font-size: 40px; letter-spacing: 1px; }
  .brand__name .brand__sub { font-size: 12.5px; letter-spacing: 3.2px; margin-top: 4px; }

  .card--back .brand { justify-content: center; margin-top: 70px; }
  .card--back .brand__dot { background: var(--white); }
  .card--back .brand__name { color: var(--white); text-align: left; }

  .services { margin-top: 38px; font-size: 17px; line-height: 1.4; }
  .services__day { font-weight: 700; }
  .services__times { margin-bottom: 10px; }
  .web-line { margin-top: 12px; font-weight: 700; font-size: 17px; letter-spacing: 4px; }

  /* Front side */
  .card--front { top: 500px; background: var(--paper); }
  .front__top { height: 128px; background: var(--white); padding: 36px 0 0 42px; }
  .card--front .brand__dot { background: var(--teal); }
  .card--front .brand__name { color: var(--ink); }
  .front__band {
    position: absolute; top: 128px; left: 0; width: 100%; height: 222px;
    background: linear-gradient(90deg, var(--teal), var(--teal-light));
    color: var(--white); padding: 20px 42px;
  }
  .person__name { font-weight: 700; font-size: 20px; letter-spacing: .5px; }
  .person__role { font-size: 16px; letter-spacing: 1px; margin-bottom: 14px; }
  .contact { list-style: none; font-size: 16px; line-height: 1.45; }
  .contact li { display: flex; align-items: center; gap: 8px; }
  .contact li.plain { padding-left: 0; }
  .contact svg { width: 15px; height: 15px; flex: none; fill: var(--white); }
  .band__circle {
    position: absolute; right: 60px; top: 30px; width: 190px; height: 190px;
    border-radius: 50%; background: rgba(255,255,255,.85);
  }
</style>
</head>
<body>
<main class="sheet">

  <section class="card card--back" aria-label="Card back">
    <div class="brand">
      <span class="brand__dot"></span>
      <p class="brand__name"><span class="brand__main">Brookvane</span><span class="brand__sub">Pentecostal Church</span></p>
    </div>
    <div class="services">
      <p class="services__day">Sunday</p>
      <p class="services__times">10am Sunday School, 11am Family Worship, 6pm Night of Prayer</p>
      <p class="services__day">Wednesday</p>
      <p class="services__times">7:30pm Adult Bible Study, Classes for all ages</p>
    </div>
    <p class="web-line">brookvane.example</p>
  </section>

  <section class="card card--front" aria-label="Card front">
    <div class="front__top">
      <div class="brand">
        <span class="brand__dot"></span>
        <p class="brand__name"><span class="brand__main">Brookvane</span><span class="brand__sub">Pentecostal Church</span></p>
      </div>
    </div>
    <div class="front__band">
      <p class="person__name">MARK ELLISON</p>
      <p class="person__role">PRESIDENT</p>
      <ul class="contact">
        <li>2718 Maple Row,</li>
        <li>Rockford, IL 61142</li>
        <li><svg viewBox="0 0 16 16" aria-hidden="true"><path d="M3 2h3l1 4-2 1a9 9 0 0 0 4 4l1-2 4 1v3a1 1 0 0 1-1 1A13 13 0 0 1 2 3a1 1 0 0 1 1-1z"/></svg>815-555-0163</li>
        <li><svg viewBox="0 0 16 16" aria-hidden="true"><path d="M1 3h14v10H1z M1 3l7 6 7-6" stroke="#4b8b99" stroke-width="1.2"/></svg>info@brookvane.example</li>
        <li><svg viewBox="0 0 16 16" aria-hidden="true"><circle cx="8" cy="8" r="7"/><path d="M1 8h14M8 1c3 3 3 11 0 14M8 1c-3 3-3 11 0 14" fill="none" stroke="#4b8b99" stroke-width="1"/></svg>www.brookvane.example</li>
      </ul>
      <span class="band__circle"></span>
    </div>
  </section>

</main>
</body>
</html>
```